Real Estate Sign - For Sale Yard Sign - Willowmere Estates

Our real estate company is looking for a new sign design to hang from in post in the front yard of the homes we are selling. Our company name is Willowmere Estates and we are open to any ideas. Attached for you is our company logo and name. The font is Trajan Pro. We are looking for a classy sign to put in front of our high end more expensive homes. You can either choose to include or not include the words "FOR SALE" on the sign (in our state, only about 1/2 of the real estate signs have room for those words. It is implied with a sign in the yard in front of a home). Thank you.

24 inches wide is important. and the height should be either 18, 24 or 30 inches. For printing purposes either of those heights will work. 18 inches is common, but some signs look great that are taller too. I'm open.

If you have any ideas for some better text options, styles or fonts, feel free to play with it.

P.S. Please feel free to play with the colors. We are not at this point set on a particular color scheme. Colors we think are nice but you may have other better ideas are black, red, white, gold, green

Target Market(s)

High end real estate home owners who choose to use our company to sell their home.

Industry/Entity Type

Real Estate

Requirements
Must have
• Company Logo
Company Name (Willowmere Estates)
Barnaby Follwick (please include my name as I am the real estate agent)
503-618-3940 (my phone number for potential clients to contact me)
Website name - willowmereestatesnw.example
***You can either choose to include the words "FOR SALE" or not***

Dimensions must be 24 inches wide. Height can be either 18, 24 or 30 inches. Must be one of those 3 heights for printing purposes.

```html
<!DOCTYPE html>
<html lang="en">
<head>
<meta charset="utf-8">
<title>Willowmere Estates – Yard Sign Sizes</title>
<link href="https://fonts.googleapis.com/css2?family=Cabin:wght@600;700&family=Archivo:wght@800&display=swap" rel="stylesheet">
<style>
  :root {
    --canvas-bg: #f3f7f8;
    --ink: #111111;
    --band: #000000;
    --brand-red: #ee0000;
    --panel-white: #ffffff;
    --panel-grey-light: #f4f4f4;
    --panel-grey-dark: #d9d9d9;
    --label: #111111;
  }
  * { margin: 0; padding: 0; box-sizing: border-box; }
  html, body { width: 1200px; height: 1000px; overflow: hidden; }
  body { background: var(--canvas-bg); position: relative; font-family: "Cabin", sans-serif; }

  .sign {
    position: absolute;
    width: 431px;
    display: flex;
    flex-direction: column;
    box-shadow: 10px 12px 14px rgba(0,0,0,0.28);
    background: var(--panel-white);
  }
  .sign--30x24 { left: 104px; top: 141px; height: 539px; }
  .sign--24x24 { left: 659px; top: 56px;  height: 431px; }
  .sign--18x24 { left: 659px; top: 598px; height: 322px; }

  .sign__band { height: 22px; background: var(--band); flex: none; }

  .sign__brand {
    height: 118px; flex: none;
    display: flex; align-items: center; justify-content: center;
    background: var(--panel-white);
  }
  .brand__name {
    font-family: "Cabin", sans-serif; font-weight: 600; color: var(--ink);
    font-size: 42px; line-height: 1; letter-spacing: 0.2px; white-space: nowrap;
  }

  .sign__body {
    flex: 1;
    display: flex; flex-direction: column; align-items: center; justify-content: center;
    background: radial-gradient(ellipse at 50% 35%, var(--panel-grey-light) 0%, #ececec 55%, var(--panel-grey-dark) 100%);
    text-align: center;
  }
  .sign__for-sale {
    font-family: "Archivo", sans-serif; font-weight: 800; color: var(--brand-red);
    line-height: 0.98; letter-spacing: 2px;
  }
  .sign--30x24 .sign__for-sale { font-size: 84px; margin-bottom: 8px; }
  .sign--24x24 .sign__for-sale { font-size: 70px; margin-bottom: 4px; }

  .sign__agent, .sign__phone {
    font-family: "Cabin", sans-serif; font-weight: 600; color: var(--ink);
    font-size: 50px; line-height: 1.1; white-space: nowrap;
  }
  .sign__agent { letter-spacing: -0.5px; }

  .sign__web {
    height: 42px; flex: none;
    background: var(--brand-red); color: var(--panel-white);
    display: flex; align-items: center; justify-content: center;
    font-family: "Cabin", sans-serif; font-weight: 700; font-size: 20px; letter-spacing: 0.3px;
    white-space: nowrap;
  }

  .size-label {
    position: absolute;
    font-family: Arial, Helvetica, sans-serif; font-size: 40px; color: var(--label);
    text-align: right; width: 200px;
  }
  .size-label--30x24 { left: 335px; top: 708px; }
  .size-label--24x24 { left: 890px; top: 510px; }
  .size-label--18x24 { left: 890px; top: 933px; }
</style>
</head>
<body>

  <section class="sign sign--30x24">
    <div class="sign__band"></div>
    <div class="sign__brand"><p class="brand__name">Willowmere Estates</p></div>
    <div class="sign__band"></div>
    <div class="sign__body">
      <p class="sign__for-sale">FOR<br>SALE</p>
      <p class="sign__agent">Barnaby Follwick</p>
      <p class="sign__phone">503-618-3940</p>
    </div>
    <div class="sign__web">www.willowmereestatesnw.example</div>
  </section>
  <p class="size-label size-label--30x24">30x24</p>

  <section class="sign sign--24x24">
    <div class="sign__band"></div>
    <div class="sign__brand"><p class="brand__name">Willowmere Estates</p></div>
    <div class="sign__band"></div>
    <div class="sign__body">
      <p class="sign__for-sale">FOR SALE</p>
      <p class="sign__agent">Barnaby Follwick</p>
      <p class="sign__phone">503-618-3940</p>
    </div>
    <div class="sign__web">www.willowmereestatesnw.example</div>
  </section>
  <p class="size-label size-label--24x24">24x24</p>

  <section class="sign sign--18x24">
    <div class="sign__band"></div>
    <div class="sign__brand"><p class="brand__name">Willowmere Estates</p></div>
    <div class="sign__band"></div>
    <div class="sign__body">
      <p class="sign__agent">Barnaby Follwick</p>
      <p class="sign__phone">503-618-3940</p>
    </div>
    <div class="sign__web">www.willowmereestatesnw.example</div>
  </section>
  <p class="size-label size-label--18x24">18x24</p>

</body>
</html>
```